Fresh Nest Builder Guide needs a new Landing Page

I like to get a landing page or website with 2-3 pages to help target home buyers who are looking to buy homes from builders such as PV Dwellings, Moritz, G.T. Falwick, etc. The landing page/website to be non-cluttered and be able to explain to home buyers that there are many benefits to include me as their buyer's agent when they buy a brand new home from any builders.
I may want to incorporate a short explanation video (animated) on the landing page and then for the viewer to click on a button that will take them to another page where they can search for new homes from different builders.
Target Market(s)
Home buyers looking to buy brand new home from builders such as PV Dwellings, Moritz, G.T. Falwick, etc.
Industry/Entity Type
Real Estate
Number of Pages Required
2 page
Requirements
Must have
- The landing page may have the explanation video at the bottom of the landing page (scrolled down) or there may be a CALL TO ACTION button that takes the viewer to the 2nd page to watch the explanation video. Once they watched the explanation video and are still interested, they can click on another CALL TO ACTION button that will take them to another website that they will be able to search for all the available new homes and register their contact information.
Should not have
- No clutters and no dark colors.

```html
<!DOCTYPE html>
<html lang="en">
<head>
<meta charset="utf-8">
<title>Fresh Nest Home Tour – New Homes From Builders</title>
<link rel="stylesheet" href="https://fonts.googleapis.com/css2?family=Open+Sans:wght@400;600;700&display=swap">
<style>
:root{
  --red:#c4524f;
  --ink:#24252d;
  --muted:#4a4c57;
  --light:#e9eef6;
  --card:#dde2ec;
  --white:#ffffff;
  --link:#5b7fd6;
}
*{box-sizing:border-box;margin:0;padding:0}
html,body{width:1200px;height:2232px;overflow:hidden}
body{font-family:"Open Sans",Arial,sans-serif;color:var(--ink);background:var(--light);position:relative}
.btn{position:absolute;display:flex;align-items:center;justify-content:center;font-size:12px;font-weight:600;border-radius:2px;text-decoration:none;white-space:nowrap}
.btn-solid{background:var(--red);color:var(--white)}
.btn-outline{border:1.5px solid var(--red);color:var(--red);background:transparent;font-weight:400}
.btn-white{background:var(--white);color:var(--red);font-weight:400}
.section-title{position:absolute;left:0;width:1200px;text-align:center;font-size:17px;font-weight:700}
.section-title::after{content:"";display:block;width:62px;height:3px;background:var(--red);margin:12px auto 0}

/* header */
.site-header{position:absolute;left:0;top:0;width:1200px;height:75px;background:var(--white);box-shadow:0 2px 6px rgba(0,0,0,.12);z-index:3}
.brand{position:absolute;left:262px;top:24px;display:flex;align-items:center;gap:8px;font-size:15px;font-weight:700;color:var(--muted)}
.brand-dot{width:12px;height:12px;border-radius:50%;background:var(--red)}
.main-nav a{position:absolute;top:29px;font-size:12px;color:var(--ink);text-decoration:none}
.main-nav .active{color:var(--red);font-weight:600}
.main-nav .active::after{content:"";position:absolute;left:-8px;right:-8px;top:42px;height:4px;background:var(--red)}
.phone-badge{position:absolute;left:796px;top:24px;width:80px;height:22px;background:var(--red);color:var(--white);border-radius:3px;font-size:9.5px;font-weight:700;display:flex;align-items:center;justify-content:center;gap:4px}

/* hero */
.hero{position:absolute;left:0;top:75px;width:1200px;height:397px;background:linear-gradient(100deg,#4a5875 0%,#7b879f 35%,#b8c0ce 60%,#6f7d99 100%)}
.hero-copy{position:absolute;left:270px;top:130px;width:440px;color:var(--white)}
.hero h1{font-size:20px;font-weight:700;line-height:30px;white-space:nowrap}
.hero-rule{width:195px;height:2px;background:var(--white);margin:5px 0 11px}
.hero p{font-size:11px;line-height:15.5px;width:225px}

/* benefits */
.benefits{position:absolute;left:0;top:472px;width:1200px;height:311px;background:var(--light)}
.benefit{position:absolute;top:70px;width:165px}
.benefit svg{display:block;width:70px;height:70px;margin-bottom:20px}
.benefit h3{font-size:12.5px;font-weight:700;margin-bottom:2px}
.benefit p{font-size:10.5px;line-height:14px}

/* video */
.video-band{position:absolute;left:0;top:783px;width:1200px;height:515px;background:linear-gradient(90deg,#2c2522 0%,#4a3f39 45%,#3a302b 100%)}
.video-band .section-title{color:var(--white)}
.video-frame{position:absolute;left:308px;top:75px;width:586px;height:326px;background:linear-gradient(120deg,#e8e8e6 0%,#b9bcbf 45%,#7d7f84 75%,#d6d3cf 100%)}
.play{position:absolute;left:260px;top:130px}
.video-text{position:absolute;left:300px;top:416px;width:600px;text-align:center;color:var(--white);font-size:12px;line-height:16px}

/* testimonials */
.testimonials{position:absolute;left:0;top:1298px;width:1200px;height:468px;background:var(--light)}
.testimonial{position:absolute;top:93px;width:177px;height:284px;background:var(--card);border-radius:3px;text-align:center}
.photo-diamond{position:absolute;left:45px;top:17px;width:87px;height:87px;transform:rotate(45deg)}
.stars{position:absolute;top:146px;left:0;width:100%;display:flex;justify-content:center}
.testimonial h3{position:absolute;top:168px;width:100%;font-size:14px;font-weight:600}
.testimonial p{position:absolute;top:200px;left:18px;width:142px;font-size:9.5px;line-height:13px;text-align:left}
.testimonial .author{position:absolute;top:263px;width:100%;font-size:10px;font-weight:600;color:var(--link)}
.slider-arrow{position:absolute;top:210px}

/* cta */
.cta-band{position:absolute;left:0;top:1766px;width:1200px;height:317px;background:linear-gradient(90deg,#262322 0%,#3d3835 50%,#555150 100%)}
.cta-band .section-title{color:var(--white)}
.cta-band .section-title span{color:var(--red)}
.cta-sub{position:absolute;left:466px;top:88px;font-size:14px;font-weight:700;color:var(--white)}
.cta-text{position:absolute;left:466px;top:112px;width:275px;text-align:center;font-size:12.5px;line-height:18px;color:var(--white)}

/* footer */
.site-footer{position:absolute;left:0;top:2083px;width:1200px;height:149px;background:var(--light)}
.footer-brand{position:absolute;left:257px;top:28px;display:flex;align-items:center;gap:8px;font-size:14px;font-weight:700;color:var(--muted)}
.footer-blurb{position:absolute;left:262px;top:72px;width:150px;font-size:9px;line-height:12px;color:var(--red)}
.footer-col{position:absolute;top:36px;font-size:10px;line-height:17px}
.footer-col h4{font-size:12px;font-weight:400;color:var(--red);margin-bottom:4px}
.footer-col a{display:block;color:var(--ink);text-decoration:none}
.contact-line{display:flex;align-items:center;gap:6px}
.social-row{display:flex;gap:6px;margin-top:4px}
.social-row span{width:11px;height:11px;background:var(--ink);border-radius:2px}
.copyright{position:absolute;left:257px;top:134px;font-size:8.5px;color:var(--red)}
.legal{position:absolute;left:772px;top:134px;font-size:8.5px;color:var(--red)}
</style>
</head>
<body>

<header class="site-header">
  <div class="brand"><span class="brand-dot"></span>Fresh Nest Home Tour</div>
  <nav class="main-nav">
    <a class="active" style="left:492px">Buy</a>
    <a style="left:546px">How I do it</a>
    <a style="left:641px">Contact Us</a>
  </nav>
  <div class="phone-badge">
    <svg width="9" height="9" viewBox="0 0 24 24"><path fill="#fff" d="M6.6 10.8a15 15 0 0 0 6.6 6.6l2.2-2.2a1 1 0 0 1 1-.25 11.4 11.4 0 0 0 3.6.57 1 1 0 0 1 1 1V20a1 1 0 0 1-1 1A17 17 0 0 1 3 4a1 1 0 0 1 1-1h3.5a1 1 0 0 1 1 1c0 1.25.2 2.45.57 3.57a1 1 0 0 1-.25 1z"/></svg>
    555-010-2022
  </div>
</header>

<section class="hero" role="img" aria-label="Bright living room with a blue door, sofa with pillows and side table, in cool blue tones">
  <div class="hero-copy">
    <h1>WE WILL SELL YOU A NEW HOME FAST<br>&amp; FOR LESS MONEY</h1>
    <div class="hero-rule"></div>
    <p>Lorem ipsum dolor sit amet, consectetur adipiscing elit. Vestibulum id convallis metus. Quisque sed varius arcu. Mauris id laoreet justo, vulputate efficitur neque.</p>
  </div>
  <a class="btn btn-solid" style="left:277px;top:276px;width:93px;height:28px">Search Homes</a>
  <a class="btn btn-white" style="left:388px;top:276px;width:95px;height:28px">Watch the video</a>
</section>

<section class="benefits">
  <h2 class="section-title" style="top:20px;font-size:15px">Benefits To Our Customers</h2>

  <div class="benefit" style="left:307px">
    <svg viewBox="0 0 70 70" fill="none" stroke="var(--red)" stroke-width="4" stroke-linecap="round"><path d="M58 35A25 25 0 1 1 50 16"/><path d="M50 8v9h9"/><path d="M33 20v16l10 8"/></svg>
    <h3>Fast &amp; Reliable</h3>
    <p>Lorem ipsum dolor sit amet, consectetur adipiscing elit. Vestibulum id convallis metus. Quisque sed varius arcu.</p>
  </div>
  <div class="benefit" style="left:530px">
    <svg viewBox="0 0 70 70" fill="none" stroke="var(--red)" stroke-width="3.5" stroke-linejoin="round"><rect x="6" y="30" width="12" height="30"/><path d="M18 33l12-14 3-14c6 0 8 6 6 14l-2 8h20c4 0 5 5 2 7 3 2 2 6-1 7 2 2 1 6-2 7 1 3-1 6-4 6H18"/></svg>
    <h3>Only reliable builders</h3>
    <p>Lorem ipsum dolor sit amet, consectetur adipiscing elit. Vestibulum id convallis metus. Quisque sed varius arcu.</p>
  </div>
  <div class="benefit" style="left:754px">
    <svg viewBox="0 0 70 70" fill="none" stroke="var(--red)" stroke-width="3" stroke-linecap="round" stroke-linejoin="round"><path d="M20 30h30a4 4 0 0 1 4 4v10a14 14 0 0 1-14 14H30a12 12 0 0 1-12-12V32z"/><path d="M26 30v-6M34 30v-8M42 30v-6M50 30v-4"/><path d="M22 64h26"/><path d="M10 14l4 4M60 12l-4 5M35 4v6M6 30h5M64 30h-5"/></svg>
    <h3>Simple &amp; Easy</h3>
    <p>Lorem ipsum dolor sit amet, consectetur adipiscing elit. Vestibulum id convallis metus. Quisque sed varius arcu.</p>
  </div>

  <a class="btn btn-outline" style="left:304px;top:255px;width:100px;height:29px">Read More</a>
  <a class="btn btn-outline" style="left:527px;top:255px;width:100px;height:29px">Read More</a>
  <a class="btn btn-outline" style="left:750px;top:255px;width:100px;height:29px">Read More</a>
</section>

<section class="video-band" role="img" aria-label="Dim interior with wooden panels and a chair, in warm brown tones">
  <h2 class="section-title" style="top:24px">Our explanation video</h2>
  <div class="video-frame" role="img" aria-label="Video still of a bright living room with a grey sofa, black chair and glass table">
    <svg class="play" width="66" height="66" viewBox="0 0 66 66"><circle cx="33" cy="33" r="31" fill="rgba(255,255,255,.35)"/><circle cx="33" cy="33" r="25" fill="var(--red)"/><path d="M27 21l18 12-18 12z" fill="#fff"/></svg>
  </div>
  <p class="video-text">Lorem ipsum dolor sit amet, consectetur adipiscing elit. Integer odio urna, ullamcorper at pretium nec, tincidunt ut ex. Quisque tincidunt facilisis enim, vitae sagittis tellus luctus ac.</p>
  <a class="btn btn-solid" style="left:548px;top:466px;width:97px;height:28px">Read More</a>
</section>

<section class="testimonials">
  <h2 class="section-title" style="top:26px">Our customers testimonials</h2>

  <svg class="slider-arrow" style="left:236px" width="24" height="50" viewBox="0 0 24 50"><path d="M20 2L4 25l16 23" fill="none" stroke="#c9cfdb" stroke-width="2"/></svg>
  <svg class="slider-arrow" style="left:968px" width="24" height="50" viewBox="0 0 24 50"><path d="M4 2l16 23L4 48" fill="none" stroke="#c9cfdb" stroke-width="2"/></svg>

  <article class="testimonial" style="left:284px">
    <div class="photo-diamond" role="img" aria-label="Modern house lit warmly at dusk" style="background:linear-gradient(135deg,#3b3331,#b27a4a 55%,#5a4a45)"></div>
    <div class="stars"><svg width="105" height="17" viewBox="0 0 105 17"><g fill="var(--red)"><path id="st" d="M8.5 0l2.1 5.6h6l-4.8 3.6 1.8 6L8.5 11.7 3.4 15.2l1.8-6L.4 5.6h6z"/><use href="#st" x="22"/><use href="#st" x="44"/><use href="#st" x="66"/><use href="#st" x="88"/></g></svg></div>
    <h3>Perfect Service</h3>
    <p>Lorem ipsum dolor sit amet, consectetur adipiscing elit. Integer odio urna, ullamcorper at pretium nec, tincidunt ut ex.</p>
    <div class="author">Paul Bright</div>
  </article>

  <article class="testimonial" style="left:521px">
    <div class="photo-diamond" role="img" aria-label="Two-storey suburban house under a blue evening sky" style="background:linear-gradient(135deg,#6a86b8,#c9d3e6 50%,#4a5a7a)"></div>
    <div class="stars"><svg width="105" height="17" viewBox="0 0 105 17"><g fill="var(--red)"><use href="#st"/><use href="#st" x="22"/><use href="#st" x="44"/><use href="#st" x="66"/><use href="#st" x="88"/></g></svg></div>
    <h3>Very Fast</h3>
    <p>Lorem ipsum dolor sit amet, consectetur adipiscing elit. Integer odio urna, ullamcorper at pretium nec, tincidunt ut ex.</p>
    <div class="author">Bella Joss</div>
  </article>

  <article class="testimonial" style="left:758px">
    <div class="photo-diamond" role="img" aria-label="Large house with lawn and trees at twilight" style="background:linear-gradient(135deg,#4a6a8a,#8aa0a8 45%,#3e5a3a)"></div>
    <div class="stars"><svg width="105" height="17" viewBox="0 0 105 17"><g fill="var(--red)"><use href="#st"/><use href="#st" x="22"/><use href="#st" x="44"/><use href="#st" x="66"/><use href="#st" x="88"/></g></svg></div>
    <h3>Super Professional</h3>
    <p>Lorem ipsum dolor sit amet, consectetur adipiscing elit. Integer odio urna, ullamcorper at pretium nec, tincidunt ut ex.</p>
    <div class="author">Alan Ames</div>
  </article>

  <a class="btn btn-solid" style="left:521px;top:401px;width:160px;height:34px">View all Testimonials</a>
</section>

<section class="cta-band" role="img" aria-label="Dark room with a dresser, dried grass in a vase and a plant, in charcoal tones">
  <h2 class="section-title" style="top:24px"><span>FIND</span> THE HOME OF YOUR DREAMS</h2>
  <div class="cta-sub">Search Homes For The Best Prices Now</div>
  <p class="cta-text">Lorem ipsum dolor sit amet, consectetur adipiscing elit. Curabitur semper turpis vitae orci fringilla elementum. Nulla sit amet lacus eleifend, aliquam leo sit amet, vestibulum elit.</p>
  <a class="btn btn-solid" style="left:521px;top:246px;width:160px;height:35px">Search Homes</a>
</section>

<footer class="site-footer">
  <div class="footer-brand"><span class="brand-dot"></span>Fresh Nest Home Tour</div>
  <p class="footer-blurb">Vestibulum volutpat, dolor sit amet laoreet malesuada.</p>

  <div class="footer-col" style="left:514px">
    <h4>Links</h4>
    <a>Buy</a><a>How We Do It</a><a>Contact Us</a>
  </div>
  <div class="footer-col" style="left:674px">
    <h4>Contact</h4>
    <div class="contact-line"><svg width="9" height="7" viewBox="0 0 9 7"><rect x=".5" y=".5" width="8" height="6" fill="none" stroke="var(--red)"/><path d="M.5.5l4 3 4-3" fill="none" stroke="var(--red)"/></svg>hello@freshnest.example</div>
    <div class="contact-line"><svg width="8" height="8" viewBox="0 0 24 24"><path fill="var(--red)" d="M6.6 10.8a15 15 0 0 0 6.6 6.6l2.2-2.2a1 1 0 0 1 1-.25 11.4 11.4 0 0 0 3.6.57 1 1 0 0 1 1 1V20a1 1 0 0 1-1 1A17 17 0 0 1 3 4a1 1 0 0 1 1-1h3.5a1 1 0 0 1 1 1c0 1.25.2 2.45.57 3.57a1 1 0 0 1-.25 1z"/></svg>555-010-4434</div>
  </div>
  <div class="footer-col" style="left:856px">
    <h4>Social</h4>
    <div class="social-row" aria-label="Social profiles"><span></span><span></span><span></span></div>
  </div>

  <div class="copyright">© 2018 Fresh Nest Home Tour. All rights reserved</div>
  <div class="legal">Terms &amp; Conditions | Privacy | Disclaimer</div>
</footer>

</body>
</html>
```